Edits to Existing Flyer

Re create this file for us with new look and feel and updated information.
Updates

Hi, We do not want/need any more submissions. The field is down to two designers. Thank you all for your time.

Target Market(s)

homeless veterans, veterans, veteran families

Font styles to use
Serif

Colors
abd036
9bcb3c
33a6d7
0255a3
3176b5

Requirements
Must have
• approved photos, readable text

```html
<!DOCTYPE html>
<html lang="en">
<head>
<meta charset="utf-8">
<title>Harbors for Valor – Supportive Services for Veteran Families</title>
<link rel="stylesheet" href="https://fonts.googleapis.com/css2?family=Tinos:wght@400;700&family=Lato:wght@400;700&display=swap">
<style>
  :root {
    --green: #9bcb3c;
    --green-bright: #abd036;
    --green-dark: #4f7d2a;
    --blue: #0255a3;
    --blue-mid: #3176b5;
    --sky: #33a6d7;
    --white: #ffffff;
    --paper: #ffffff;
    --canvas: #f4f4f4;
    --serif: "Tinos", "Times New Roman", serif;
    --sans: "Lato", "Helvetica Neue", Arial, sans-serif;
  }
  * { box-sizing: border-box; margin: 0; padding: 0; }
  html, body {
    width: 1200px; height: 1200px; overflow: hidden;
    background: var(--canvas);
  }
  .spread {
    position: absolute; left: 30px; top: 194px;
    width: 1140px; height: 812px;
    display: flex;
  }
  .panel { position: relative; width: 570px; height: 812px; overflow: hidden; }

  /* back cover */
  .back { background: var(--green); }
  .back__hero {
    position: absolute; left: 0; top: 0; width: 570px; height: 290px;
    background: linear-gradient(180deg, #8fbf3a 0%, #a2cf48 55%, var(--green) 100%);
  }
  .brand-name {
    font-family: var(--serif); font-weight: 400; letter-spacing: 1px;
    text-transform: uppercase; white-space: nowrap;
  }
  .back__brand {
    position: absolute; left: 0; width: 570px; top: 290px;
    text-align: center; color: var(--white); font-size: 15px;
  }
  .back__mark {
    display: block; width: 46px; height: 46px; margin: 0 auto 10px;
    border-radius: 50%; background: var(--white);
  }
  .back__map {
    position: absolute; left: 142px; top: 340px; width: 297px; height: 138px;
    border: 3px solid var(--blue); border-radius: 12px;
    background: linear-gradient(135deg, #eeeae2 0%, #e4e1d8 60%, #ece6c4 100%);
  }
  .back__org {
    position: absolute; left: 0; width: 570px; top: 505px;
    text-align: center; color: var(--blue);
    font-family: var(--serif); font-weight: 700; font-size: 13px; line-height: 16px;
    text-transform: uppercase;
  }
  .contact {
    position: absolute; left: 0; width: 570px; top: 545px;
    list-style: none; text-align: center;
    color: var(--white); font-family: var(--sans); font-size: 12.5px; line-height: 24px;
  }
  .contact svg { width: 11px; height: 11px; vertical-align: -1px; margin-right: 3px; fill: var(--blue); }
  .back__band { position: absolute; left: 0; top: 0; }
  .partners {
    position: absolute; top: 752px; left: 0; width: 570px;
    display: flex; justify-content: flex-end; gap: 36px; padding-right: 64px;
    color: var(--white); font-family: var(--serif); font-size: 10px; line-height: 11px;
  }
  .partner { display: flex; align-items: center; gap: 6px; }
  .partner__badge { width: 26px; height: 26px; border-radius: 50%; background: var(--white); opacity: .9; }
  .partner__badge--square { border-radius: 3px; width: 20px; height: 20px; }

  /* front cover */
  .front { background: var(--paper); }
  .front::before {
    content: ""; position: absolute; left: 0; top: 0; width: 30px; height: 100%;
    background: linear-gradient(90deg, rgba(0,0,0,.06), rgba(0,0,0,0));
    z-index: 2;
  }
  .front__brand {
    position: absolute; left: 0; width: 570px; top: 120px;
    text-align: center; color: var(--green-dark); font-size: 25px; font-weight: 700;
    display: flex; justify-content: center; align-items: center; gap: 10px;
  }
  .front__mark { width: 22px; height: 22px; border-radius: 50%; background: #7a5f33; }
  .front__art { position: absolute; left: 0; top: 0; }
  .front__title {
    position: absolute; left: 0; width: 570px; top: 660px; text-align: center;
    font-family: var(--serif);
  }
  .front__title-lead { display: block; color: var(--blue); font-weight: 700; font-size: 37px; line-height: 42px; }
  .front__title-main { display: block; color: var(--green); font-weight: 400; font-size: 54px; line-height: 56px; }
  .front__url {
    position: absolute; left: 0; width: 570px; top: 768px; text-align: center;
    font-family: var(--serif); color: var(--blue); font-size: 12px; letter-spacing: 9px;
  }
</style>
</head>
<body>
<main class="spread">

  <section class="panel back">
    <div class="back__hero" role="img" aria-label="Faded green-tinted photo of a service member embracing a loved one"></div>

    <div class="back__brand">
      <span class="back__mark"></span>
      <span class="brand-name">Harbors for Valor</span>
    </div>

    <div class="back__map" role="img" aria-label="Street map showing the office location"></div>

    <p class="back__org">Bayside Community Renewal Project<br>Harbors for Valor</p>

    <ul class="contact">
      <li><svg viewBox="0 0 24 24"><path d="M6.6 10.8a15.1 15.1 0 0 0 6.6 6.6l2.2-2.2a1 1 0 0 1 1-.25 11.4 11.4 0 0 0 3.6.57 1 1 0 0 1 1 1V20a1 1 0 0 1-1 1A17 17 0 0 1 3 4a1 1 0 0 1 1-1h3.5a1 1 0 0 1 1 1c0 1.25.2 2.45.57 3.57a1 1 0 0 1-.25 1z"/></svg>555.014.2870</li>
      <li><svg viewBox="0 0 24 24"><path d="M12 2a7 7 0 0 0-7 7c0 5.2 7 13 7 13s7-7.8 7-13a7 7 0 0 0-7-7zm0 9.5A2.5 2.5 0 1 1 12 6.5a2.5 2.5 0 0 1 0 5z"/></svg>1840 LINDEN AVE. MAPLEWOOD, CA 95012</li>
      <li>community.page/harborsforvalor</li>
      <li><svg viewBox="0 0 24 24"><circle cx="12" cy="12" r="10"/></svg>www.bcrp-example.org</li>
    </ul>

    <svg class="back__band" width="570" height="812" viewBox="0 0 570 812" aria-hidden="true">
      <polygon points="0,733 570,642 570,650 0,741" fill="var(--white)"/>
      <polygon points="0,741 570,650 570,812 0,812" fill="var(--blue)"/>
    </svg>

    <div class="partners">
      <div class="partner"><span class="partner__badge partner__badge--square"></span><span>Bayside Community<br>Renewal Project</span></div>
      <div class="partner"><span class="partner__badge"></span><span>St. Anselm Aid<br>Lakeshore County</span></div>
    </div>
  </section>

  <section class="panel front">
    <div class="front__brand">
      <span class="front__mark"></span>
      <span class="brand-name">Harbors for Valor</span>
    </div>

    <svg class="front__art" width="570" height="812" viewBox="0 0 570 812">
      <defs>
        <linearGradient id="photoTone" x1="0" y1="0" x2="1" y2="1">
          <stop offset="0" stop-color="#6b5a52"/>
          <stop offset=".35" stop-color="#9a7e74"/>
          <stop offset=".65" stop-color="#a89477"/>
          <stop offset="1" stop-color="#d9d6d2"/>
        </linearGradient>
      </defs>
      <polygon points="0,168 570,262 570,400 0,190" fill="var(--green)"/>
      <polygon points="0,178 570,396 570,404 0,186" fill="var(--blue)"/>
      <polygon points="0,190 570,408 570,412 0,194" fill="var(--white)"/>
      <polygon points="0,196 570,414 570,532 0,630" fill="url(#photoTone)" role="img" aria-label="Photo of a smiling service member in camouflage lifting a baby into the air"/>
      <polygon points="0,630 570,532 570,546 0,644" fill="var(--green)"/>
      <polygon points="0,644 570,546 570,550 0,648" fill="var(--white)"/>
      <polygon points="0,648 570,550 570,556 0,654" fill="var(--blue)"/>
    </svg>

    <h1 class="front__title">
      <span class="front__title-lead">Supportive Services for</span>
      <span class="front__title-main">Veteran Families</span>
    </h1>
    <p class="front__url">www.bcrp-example.org</p>
  </section>

</main>
</body>
</html>
```